10-year customer thank you card

We want a greeting card that our sales reps can send to companies/customers who have been with our company for 10 or more years. We're a software company, our corporate color is blue but we also like green, orange, and purple. We'd like something rather minimal/simplistic for this card, perhaps building off our tree logo. We're really open to ideas for this one. You must use the template files that are uploaded. Copy included in 10 year thank you card file; the copy may change based on how it looks when laid out
Updates

I updated our brief. We'd prefer a sans serif font. I also uploaded a blank infographic image that includes more of our approved colors.

Industry/Entity Type

Software

Font styles to use
Sans Serif

```html
<!DOCTYPE html>
<html lang="en">
<head>
<meta charset="utf-8">
<title>Ten Years — Thank You Card</title>
<link rel="stylesheet" href="https://fonts.googleapis.com/css2?family=Bodoni+Moda:wght@500;700&family=Open+Sans:wght@400;600&display=swap">
<style>
  :root {
    --slate: #3d5a6c;
    --orange: #e8603c;
    --white: #ffffff;
    --ink: #1d4f86;
  }
  html, body {
    margin: 0;
    padding: 0;
    width: 869px;
    height: 1200px;
    overflow: hidden;
    background: var(--white);
  }
  .card {
    position: relative;
    width: 869px;
    height: 1200px;
    background: var(--white);
    font-family: "Open Sans", Arial, sans-serif;
  }
  .front-panel {
    position: absolute;
    left: 0;
    top: 0;
    width: 869px;
    height: 593px;
    background: var(--slate);
    transform: rotate(180deg);
  }
  .rule {
    position: absolute;
    top: 523px;
    height: 3px;
    background: var(--orange);
  }
  .rule-left { left: 0; width: 345px; }
  .rule-right { left: 540px; right: 0; }
  .thanks {
    position: absolute;
    left: 345px;
    width: 195px;
    top: 502px;
    height: 46px;
    display: flex;
    align-items: center;
    justify-content: center;
    color: var(--white);
    font-size: 22px;
    letter-spacing: 1px;
    text-transform: uppercase;
  }
  .thanks .brace {
    color: var(--orange);
    font-size: 46px;
    font-weight: 400;
    line-height: 1;
    margin: 0 8px;
  }
  .milestone {
    position: absolute;
    left: 0;
    right: 0;
    text-align: center;
    font-family: "Bodoni Moda", Georgia, serif;
  }
  .milestone-number {
    top: 150px;
    font-size: 200px;
    font-weight: 700;
    line-height: 1;
    color: var(--orange);
    letter-spacing: -4px;
  }
  .milestone-label {
    top: 334px;
    font-size: 66px;
    font-weight: 500;
    line-height: 1;
    color: var(--white);
    letter-spacing: 2px;
  }
  .brand {
    position: absolute;
    left: 0;
    right: 0;
    top: 1084px;
    text-align: center;
  }
  .brand-name {
    display: inline-flex;
    align-items: center;
    gap: 14px;
    color: var(--ink);
    font-size: 48px;
    font-weight: 600;
    line-height: 1;
    letter-spacing: -0.5px;
  }
  .brand-dot {
    width: 34px;
    height: 34px;
    border-radius: 50%;
    background: var(--ink);
  }
  .brand-url {
    margin-top: 10px;
    color: var(--orange);
    font-size: 27px;
    font-weight: 400;
  }
</style>
</head>
<body>
  <main class="card">
    <section class="front-panel">
      <div class="rule rule-left"></div>
      <div class="thanks"><span class="brace">{</span>Thank You<span class="brace">}</span></div>
      <div class="rule rule-right"></div>
      <div class="milestone milestone-number">10</div>
      <div class="milestone milestone-label">YEARS</div>
    </section>
    <footer class="brand">
      <div class="brand-name"><span class="brand-dot"></span>Tidewell Software</div>
      <div class="brand-url">www.tidewell.com</div>
    </footer>
  </main>
</body>
</html>
```